Cruise & Resort Travel Redemption Vouchers

Need to have all of these pages completely re-done. These designs are horrible and need to look much more professional. The individual vouchers like the "silver gull laugh house" & Crimson lantern feast can look similar to the design on their websites.
New york link
http://gulllaughsfl.com/
Crimson Lantern Feast
http://www.crimson-lantern.com/
Please do something with the tiny anchors all over the place. Or just get rid of them.
Does not need to be over the top design heavy...just professional and simple with small doses of vacation added.
Updates
get rid of the stupid anchors all over the place.
Target Market(s)
35-60
Industry/Entity Type
Club
Requirements
Must have
- All pages done.
The company logo on the pages,found here.
http://harborgetawayoffers.com/
The Abbreviation is R.T.B

```html
<!DOCTYPE html>
<html lang="en">
<head>
<meta charset="utf-8">
<title>Travel Redemption Vouchers</title>
<link href="https://fonts.googleapis.com/css2?family=EB+Garamond:ital,wght@0,400;0,600;1,400&family=Montserrat:wght@800&display=swap" rel="stylesheet">
<style>
:root{
  --ink:#1f1d1e;
  --bar:#231f20;
  --bar-text:#ffffff;
  --paper:rgba(255,255,255,.95);
  --dash:#555555;
  --backdrop:#3a3a3a;
  --sky-deep:#3f97d6;
  --sky-mid:#9fd0f0;
  --cloud:#f3f9fd;
  --sea:#4cc0cf;
  --sand:#ece6da;
  --lantern-gold:#f3d27a;
  --lantern-haze:#fbeec8;
  --bokeh-red:#e2483b;
  --bokeh-orange:#f39a3a;
  --bokeh-yellow:#f6df6a;
  --bokeh-teal:#4fb3c4;
}
*{box-sizing:border-box;margin:0;padding:0}
html,body{width:1200px;height:660px;overflow:hidden;background:var(--backdrop)}
.stage{position:absolute;left:0;top:0;width:1345px;height:740px;transform:scale(.8922);transform-origin:0 0;font-family:"EB Garamond",Georgia,serif;color:var(--ink);font-size:9px}
.page{position:absolute;top:4px;height:733px;overflow:hidden}
.page--left{left:105px;width:563px}
.page--right{left:675px;width:655px}
.page-backdrop{position:absolute;inset:0;background:linear-gradient(180deg,var(--sky-deep) 0%,var(--sky-mid) 14%,var(--cloud) 38%,var(--sky-mid) 52%,var(--cloud) 62%,var(--sea) 78%,var(--sand) 82%,var(--sand) 100%)}
.coupon{position:absolute;width:535px;height:277px;background:var(--paper);border:3px dashed var(--dash);border-radius:12px}
.coupon--top{top:24px}
.coupon--bottom{top:359px}
.page--left .coupon{left:15px}
.page--right .coupon{left:15px}
.col{position:absolute;top:15px;width:238px;display:flex;flex-direction:column}
.col--left{left:14px}
.col--right{left:277px;text-align:center}
.bar{background:var(--bar);color:var(--bar-text);font-family:"Montserrat",Arial,sans-serif;font-weight:800;font-size:11px;letter-spacing:.3px;text-align:center;line-height:17px;height:17px;text-transform:uppercase}
.bar--double{height:34px;line-height:14px;padding-top:3px}
.note{line-height:12px;text-align:center}
.field{display:flex;align-items:flex-end;gap:3px;height:15px;line-height:12px;white-space:nowrap}
.rule{flex:1;border-bottom:1px solid var(--ink);height:10px}
.rule--s{flex:0 0 26px}
.rule--m{flex:0 0 55px}
.rule--ph{flex:0 0 12px}
.package{display:flex;justify-content:center;align-items:center;gap:4px;height:18px}
.package-box{width:93px;height:17px;border:1px solid var(--ink)}
.date-row{display:flex;justify-content:center;align-items:flex-end;gap:5px;height:14px}
.date-row .rule{flex:0 0 75px}
.date-hint{display:flex;justify-content:center;gap:48px;font-style:italic;font-size:8px;height:11px}
.date-hint--single{justify-content:flex-end;padding-right:25px}
.strong{font-weight:600}
.small-note{font-style:italic;font-size:7px;text-align:left;margin-top:2px}
.blank-line{border-bottom:1px solid var(--ink);height:12px}
.interest{position:relative;height:70px}
.interest-label{position:absolute;right:10px;top:4px;font-weight:600}
.interest-rule{position:absolute;right:22px;top:32px;width:72px;border-bottom:1px solid var(--ink);height:0}
.interest-hint{position:absolute;right:28px;top:20px;font-style:italic;font-size:8px}
.venue-name{position:absolute;left:8px;top:18px;font-size:17px;line-height:19px;text-align:left;width:100px}
.art{position:absolute}
.art--lantern{left:150px;top:95px;width:190px;height:180px;background:radial-gradient(ellipse at 50% 60%,var(--lantern-gold) 0%,var(--lantern-haze) 45%,rgba(255,255,255,0) 72%);opacity:.85}
.art--bokeh{left:275px;top:0;width:254px;height:271px;border-radius:0 9px 9px 0;background:radial-gradient(circle at 25% 30%,var(--bokeh-yellow) 0%,rgba(246,223,106,0) 35%),radial-gradient(circle at 70% 45%,var(--bokeh-red) 0%,rgba(226,72,59,0) 45%),radial-gradient(circle at 85% 85%,var(--bokeh-teal) 0%,rgba(79,179,196,0) 35%),linear-gradient(135deg,var(--bokeh-orange),#b8493f 60%,#7a7f86);opacity:.8}
.footer{position:absolute;left:117px;display:flex;gap:18px;align-items:flex-start;line-height:11px;font-size:8.5px}
.footer--top{top:316px}
.footer--bottom{top:651px}
.brand{display:flex;align-items:center;gap:4px;margin-top:6px;font-size:8px;font-weight:600;white-space:nowrap}
.brand-dot{width:16px;height:16px;border-radius:50%;background:var(--ink)}
.footer-call{font-style:italic}
</style>
</head>
<body>
<div class="stage">

  <!-- Reservation page -->
  <section class="page page--left">
    <div class="page-backdrop" role="img" aria-label="Tropical sky with clouds over a sea horizon and white sand beach"></div>

    <div class="coupon coupon--top">
      <div class="col col--left">
        <div class="bar">Reservation Form</div>
        <p class="note" style="margin-top:10px">Enjoy 3 Days and 2 Nights in Ft. Lauderdale, FL</p>
        <div class="package" style="margin-top:8px">Package #: <span class="package-box"></span></div>
        <div class="bar" style="margin-top:14px">Traveler Information</div>
        <div style="margin-top:8px">
          <div class="field">Primary Traveler: <span class="rule"></span></div>
          <div class="field">Second Traveler: <span class="rule"></span></div>
          <div class="field">Third Traveler: <span class="rule"></span></div>
          <div class="field">Fourth Traveler: <span class="rule"></span></div>
          <div class="field">Address:</div>
          <div class="field">City: <span class="rule"></span> State: <span class="rule rule--s"></span> Zip: <span class="rule rule--m"></span></div>
          <div class="field">Day Ph.: (<span class="rule rule--ph"></span>)<span class="rule"></span> Evening Ph: (<span class="rule rule--ph"></span>)<span class="rule"></span></div>
          <div class="field">Best time to be reached:</div>
          <div class="field">between <span class="rule"></span> am/pm and <span class="rule"></span> am/pm</div>
        </div>
      </div>
      <div class="col col--right">
        <div class="bar bar--double">Travel Date (Change) Request<br>Information</div>
        <p class="note" style="margin-top:6px">Reservation Form must be received at least 60 days prior to your earliest requested arrival date.<br>Or Call for reservations: 1-888-555-0147</p>
        <p class="strong" style="margin-top:6px">Arrival Date and Departure Date</p>
        <div class="date-row" style="margin-top:4px"><span class="rule"></span> and <span class="rule"></span></div>
        <div class="date-hint"><span>MM/DD/YY</span><span>MM/DD/YY</span></div>
        <div class="field" style="margin-top:6px">Additional Required by/Request: <span class="rule"></span></div>
        <div class="blank-line"></div>
        <div class="bar" style="margin-top:8px">Required to Process</div>
        <p class="note" style="margin-top:5px">I/We have read and understand fully all the Terms and Conditions of this Attraction, as distinguished on this Attraction Ticket Voucher.</p>
        <div class="field" style="margin-top:10px">Signature: <span class="rule"></span> Date: <span class="rule"></span></div>
        <p class="small-note">*Required for processing reservation request.</p>
      </div>
    </div>

    <div class="footer footer--top">
      <div class="brand"><span class="brand-dot"></span>Harbor Getaway Offers</div>
      <div>SEND FORM TO: ATTN Shipping Dept.<br>820 Seabreeze Harbor Way, Coral Point, FL 33400 USA<br><span class="footer-call">Or simply call to confirm 1-888-555-0147 Option #1</span></div>
    </div>

    <div class="coupon coupon--bottom">
      <div class="col col--left">
        <div class="bar">Reservation Form</div>
        <p class="note" style="margin-top:10px">Enjoy 3 Days and 2 Nights in Ft. Lauderdale, FL</p>
        <div class="package" style="margin-top:8px">Package #: <span class="package-box"></span></div>
        <div class="bar" style="margin-top:14px">Traveler Information</div>
        <div style="margin-top:8px">
          <div class="field">Primary Traveler: <span class="rule"></span></div>
          <div class="field">Second Traveler: <span class="rule"></span></div>
          <div class="field">Third Traveler: <span class="rule"></span></div>
          <div class="field">Fourth Traveler: <span class="rule"></span></div>
          <div class="field">Address:</div>
          <div class="field">City: <span class="rule"></span> State: <span class="rule rule--s"></span> Zip: <span class="rule rule--m"></span></div>
          <div class="field">Day Ph.: (<span class="rule rule--ph"></span>)<span class="rule"></span> Evening Ph: (<span class="rule rule--ph"></span>)<span class="rule"></span></div>
          <div class="field">Best time to be reached:</div>
          <div class="field">between <span class="rule"></span> am/pm and <span class="rule"></span> am/pm</div>
        </div>
      </div>
      <div class="col col--right">
        <div class="bar bar--double">Travel Date (Change) Request<br>Information</div>
        <p class="note" style="margin-top:6px">Reservation Form must be received at least 60 days prior to your earliest requested arrival date.<br>Or Call for reservations: 1-888-555-0147</p>
        <p class="strong" style="margin-top:6px">Arrival Date and Departure Date</p>
        <div class="date-row" style="margin-top:4px"><span class="rule"></span> and <span class="rule"></span></div>
        <div class="date-hint"><span>MM/DD/YY</span><span>MM/DD/YY</span></div>
        <div class="field" style="margin-top:6px">Additional Required by/Request: <span class="rule"></span></div>
        <div class="blank-line"></div>
        <div class="bar" style="margin-top:8px">Required to Process</div>
        <p class="note" style="margin-top:5px">I/We have read and understand fully all the Terms and Conditions of this Attraction, as distinguished on this Attraction Ticket Voucher.</p>
        <div class="field" style="margin-top:10px">Signature: <span class="rule"></span> Date: <span class="rule"></span></div>
        <p class="small-note">*Required for processing reservation request.</p>
      </div>
    </div>

    <div class="footer footer--bottom">
      <div class="brand"><span class="brand-dot"></span>Harbor Getaway Offers</div>
      <div>SEND FORM TO: ATTN Shipping Dept.<br>820 Seabreeze Harbor Way, Coral Point, FL 33400 USA<br><span class="footer-call">Or simply call to confirm 1-888-555-0147 Option #1</span></div>
    </div>
  </section>

  <!-- Attraction voucher page -->
  <section class="page page--right">
    <div class="page-backdrop" role="img" aria-label="Tropical sky with clouds over a sea horizon and white sand beach"></div>

    <div class="coupon coupon--top">
      <div class="art art--lantern" role="img" aria-label="Soft golden glow behind a palace silhouette for the dinner show"></div>
      <div class="col col--left">
        <div class="bar">Attraction Ticket Voucher</div>
        <p class="note" style="margin-top:5px">Present This Voucher at our Welcome Center for:<br>Two tickets to Crimson Lantern Feast &amp; Show of Orlando, FL.<br>*Addition Guests may pre-pay/purchase additional tickets at our current rate:<br>Currently $27.00 each. Retail Value per ticket is $62.00.</p>
        <div class="package" style="margin-top:6px">Package #: <span class="package-box"></span></div>
        <div class="bar" style="margin-top:6px">Ticket Holder Information</div>
        <div style="margin-top:6px">
          <div class="field">Primary Guest: <span class="rule"></span></div>
          <div class="field">Second Guest: <span class="rule"></span></div>
          <div class="field">Third Guest: <span class="rule"></span></div>
          <div class="field">Fourth Guest: <span class="rule"></span></div>
          <div class="field">Address:</div>
          <div class="field">City: <span class="rule"></span> State: <span class="rule rule--s"></span> Zip: <span class="rule rule--m"></span></div>
          <div class="field">Day Ph.: (<span class="rule rule--ph"></span>)<span class="rule"></span> Evening Ph: (<span class="rule rule--ph"></span>)<span class="rule"></span></div>
        </div>
      </div>
      <div class="col col--right">
        <div class="bar">Attraction Date of Interest</div>
        <p class="note" style="margin-top:4px">Reservation Form must be received at least 60 days prior to your earliest requested arrival date.<br>Or Call for reservations: 1-888-555-0147</p>
        <div class="interest">
          <span class="venue-name">Crimson Lantern</span>
          <span class="interest-label">Attraction Date of Interest</span>
          <span class="interest-hint">MM/DD/YY</span>
          <span class="interest-rule"></span>
        </div>
        <div class="field">Additional Required by/Request: <span class="rule"></span></div>
        <div class="blank-line"></div>
        <div class="bar" style="margin-top:8px">Required to Process</div>
        <p class="note" style="margin-top:5px">I/We have read and understand fully all the Terms and Conditions of this Attraction, as distinguished on this Attraction Ticket Voucher.</p>
        <div class="field" style="margin-top:10px">Signature: <span class="rule"></span> Date: <span class="rule"></span></div>
        <p class="small-note">*Required for processing reservation request.</p>
      </div>
    </div>

    <div class="footer footer--top">
      <div class="brand"><span class="brand-dot"></span>Harbor Getaway Offers</div>
      <div>SEND FORM TO: ATTN Shipping Dept.<br>820 Seabreeze Harbor Way, Coral Point, FL 33400 USA<br><span class="footer-call">Or simply call to confirm 1-888-555-0147 Option #1</span></div>
    </div>

    <div class="coupon coupon--bottom">
      <div class="art art--bokeh" role="img" aria-label="Colourful blurred stage lights for the comedy club"></div>
      <div class="col col--left">
        <div class="bar">Attraction Ticket Voucher</div>
        <p class="note" style="margin-top:5px">Present This Voucher at our Welcome Center for:<br>VIP Admission for up to Four Ticket to the<br>Silver Gull Laugh House of Boca Raton, FL.<br>* Two item minimum purchase required.</p>
        <div class="package" style="margin-top:6px">Package #: <span class="package-box"></span></div>
        <div class="bar" style="margin-top:18px">Ticket Holder Information</div>
        <div style="margin-top:6px">
          <div class="field">Primary Guest: <span class="rule"></span></div>
          <div class="field">Second Guest: <span class="rule"></span></div>
          <div class="field">Third Guest: <span class="rule"></span></div>
          <div class="field">Fourth Guest: <span class="rule"></span></div>
          <div class="field">Address:</div>
          <div class="field">City: <span class="rule"></span> State: <span class="rule rule--s"></span> Zip: <span class="rule rule--m"></span></div>
          <div class="field">Day Ph.: (<span class="rule rule--ph"></span>)<span class="rule"></span> Evening Ph: (<span class="rule rule--ph"></span>)<span class="rule"></span></div>
        </div>
      </div>
      <div class="col col--right">
        <div class="bar">Attraction Date of Interest</div>
        <p class="note" style="margin-top:4px">Reservation Form must be received at least 60 days prior to your earliest requested arrival date.<br>Or Call for reservations: 1-888-555-0147</p>
        <div class="interest">
          <span class="venue-name">Silver Gull Laugh House</span>
          <span class="interest-label">Attraction Date of Interest</span>
          <span class="interest-hint">MM/DD/YY</span>
          <span class="interest-rule"></span>
        </div>
        <div class="field">Additional Required by/Request: <span class="rule"></span></div>
        <div class="blank-line"></div>
        <div class="bar" style="margin-top:8px">Required to Process</div>
        <p class="note" style="margin-top:5px">I/We have read and understand fully all the Terms and Conditions of this Attraction, as distinguished on this Attraction Ticket Voucher.</p>
        <div class="field" style="margin-top:10px">Signature: <span class="rule"></span> Date: <span class="rule"></span></div>
        <p class="small-note">*Required for processing reservation request.</p>
      </div>
    </div>

    <div class="footer footer--bottom">
      <div class="brand"><span class="brand-dot"></span>Harbor Getaway Offers</div>
      <div>SEND FORM TO: ATTN Shipping Dept.<br>820 Seabreeze Harbor Way, Coral Point, FL 33400 USA<br><span class="footer-call">Or simply call to confirm 1-888-555-0147 Option #1</span></div>
    </div>
  </section>

</div>
</body>
</html>
```